Commercial Bakery needs packing design for a Bread Bag.

Dorne's Bakery needs a design for a bread bag to be distributed to grocery stores. We make all kinds of breads and want this packaging to represent our company. We would like the packaging to be black and white with a fun/bubbly modern design. I have attached a few ideas of what I am looking for.
There are 5 different products. Packaging must be the same for each product except for corresponding product name, bar code and nutrional facts.
Product names:
Coconut Cream Bread
Cream Bread
Potato Rolls
Roll ups
Coconut & Raisin Bread

Our products are packaged in a 11” x 8” poly bag.
I will open 5 contracts with whoever’s design I select. I will then provide nutritional facts, barcodes for items once a contract is selected. Thank you!!

Target Market(s)

Grocery stores

Industry/Entity Type

Bakery

Requirements
Must have
• Black and White (off whites are ok)
Should not have
• Color

```html
<!DOCTYPE html>
<html lang="en">
<head>
<meta charset="UTF-8">
<title>Dorne's Bakery – Coconut Cream Bread Bag</title>
<link rel="stylesheet" href="https://fonts.googleapis.com/css2?family=Kalam:wght@700&family=Source+Sans+3:wght@400;600&family=Didact+Gothic&family=Montserrat:wght@600&family=Oswald:wght@300;500&family=Tinos:ital@1&display=swap">
<style>
  :root {
    --ink: #000000;
    --paper: #f4f2ec;
    --rule: #ffffff;
  }
  * { margin: 0; padding: 0; box-sizing: border-box; }
  html, body { width: 1200px; height: 829px; overflow: hidden; background: var(--ink); }
  .canvas { position: relative; width: 1200px; height: 829px; background: var(--ink); color: var(--ink); }

  .panel-frame { position: absolute; border: 1px solid var(--rule); }
  .panel-frame.front { left: 13px; top: 15px; width: 582px; height: 799px; }
  .panel-frame.back { left: 606px; top: 15px; width: 582px; height: 799px; }

  .paper { position: absolute; }
  .front-paper { left: 14px; top: 380px; width: 580px; height: 433px; }
  .back-paper { left: 642px; top: 52px; width: 509px; height: 725px; }

  .abs { position: absolute; }

  /* front */
  .brand { left: 14px; width: 580px; top: 462px; text-align: center; font-family: "Source Sans 3", sans-serif; font-weight: 600; font-size: 34px; letter-spacing: 1px; }
  .brand .dot { display: inline-block; width: 14px; height: 14px; border-radius: 50%; background: var(--ink); margin-right: 12px; vertical-align: middle; }
  .product-name { left: 14px; width: 580px; top: 580px; text-align: center; font-family: "Kalam", cursive; font-weight: 700; font-size: 72px; letter-spacing: 1px; line-height: 1; }
  .product-type { left: 14px; width: 580px; top: 672px; text-align: center; font-family: "Source Sans 3", sans-serif; font-size: 60px; line-height: 1; }
  .double-rule { position: absolute; top: 701px; width: 60px; height: 7px; border-top: 2px solid var(--ink); border-bottom: 2px solid var(--ink); }
  .double-rule.left { left: 154px; }
  .double-rule.right { left: 393px; }
  .netto { left: 14px; width: 580px; top: 773px; text-align: center; font-family: "Source Sans 3", sans-serif; font-size: 17px; }

  /* nutrition */
  .nutrition { left: 739px; top: 83px; width: 315px; height: 332px; border: 1px solid var(--ink); font-family: "Oswald", sans-serif; font-weight: 300; font-size: 8.5px; padding: 0 7px; }
  .nutrition h2 { font-weight: 500; font-size: 10.5px; letter-spacing: 2px; margin-top: 2px; height: 22px; line-height: 22px; }
  .nrow { display: grid; grid-template-columns: 1fr 50px 56px; height: 14px; line-height: 14px; }
  .nrow .amt { text-align: center; font-size: 6.5px; letter-spacing: 1px; }
  .nrow .pct { text-align: right; font-size: 6.5px; letter-spacing: 1px; font-weight: 500; }
  .nrow.bold .lbl { font-weight: 500; }
  .nrow.sub .lbl { padding-left: 11px; }
  .nrow.head { font-weight: 500; }
  .gap { height: 6px; }
  .bar-thick { height: 3px; background: var(--ink); margin: 1px -7px 3px; }
  .bar-thin { height: 2px; background: var(--ink); margin: 2px -7px 3px; }
  .dv-head { text-align: right; font-weight: 500; font-size: 11px; height: 18px; line-height: 18px; }
  .footnote { font-family: "Tinos", serif; font-style: italic; font-size: 7px; line-height: 10px; padding-left: 8px; text-indent: -8px; }

  /* ingredients & contact */
  .heading { font-family: "Montserrat", sans-serif; font-weight: 600; font-size: 17px; letter-spacing: 2px; }
  .ingredients-title { left: 657px; top: 436px; }
  .ingredients-title small { font-size: 9px; }
  .ingredients { left: 657px; top: 470px; width: 240px; font-family: "Didact Gothic", sans-serif; font-size: 11.6px; line-height: 13.8px; letter-spacing: 1px; }

  .contact { left: 880px; width: 290px; text-align: center; font-family: "Didact Gothic", sans-serif; font-size: 10px; letter-spacing: 1px; line-height: 13px; }
  .producer-title { left: 880px; width: 290px; top: 436px; text-align: center; font-size: 15px; }
  .producer { top: 465px; }
  .service-title { left: 880px; width: 290px; top: 530px; text-align: center; font-size: 15px; }
  .service { top: 565px; line-height: 15.5px; }

  .disposal { left: 911px; top: 668px; display: flex; gap: 16px; }
  .dates { left: 912px; top: 716px; font-family: "Didact Gothic", sans-serif; font-size: 12.5px; letter-spacing: 1.5px; line-height: 15px; }
</style>
</head>
<body>
<main class="canvas">
  <div class="panel-frame front"></div>
  <div class="panel-frame back"></div>

  <!-- front panel paper with sawtooth edges -->
  <svg class="paper front-paper" width="580" height="433" viewBox="0 0 580 433" aria-hidden="true">
    <defs>
      <pattern id="teeth-down" width="29" height="15" patternUnits="userSpaceOnUse">
        <polygon points="0,0 29,0 14.5,15" fill="#000"/>
      </pattern>
      <pattern id="teeth-up" width="29" height="14" patternUnits="userSpaceOnUse">
        <polygon points="0,14 29,14 14.5,0" fill="#000"/>
      </pattern>
    </defs>
    <rect width="580" height="433" fill="#f4f2ec"/>
    <rect width="580" height="15" fill="url(#teeth-down)"/>
    <rect y="419" width="580" height="14" fill="url(#teeth-up)"/>
  </svg>

  <!-- back panel paper with sawtooth edges -->
  <svg class="paper back-paper" width="509" height="725" viewBox="0 0 509 725" aria-hidden="true">
    <defs>
      <pattern id="back-teeth-down" width="28.3" height="14" patternUnits="userSpaceOnUse">
        <polygon points="0,0 28.3,0 14.15,14" fill="#000"/>
      </pattern>
      <pattern id="back-teeth-up" width="28.3" height="14" patternUnits="userSpaceOnUse">
        <polygon points="0,14 28.3,14 14.15,0" fill="#000"/>
      </pattern>
    </defs>
    <rect width="509" height="725" fill="#f4f2ec"/>
    <rect width="509" height="14" fill="url(#back-teeth-down)"/>
    <rect y="711" width="509" height="14" fill="url(#back-teeth-up)"/>
  </svg>

  <!-- front -->
  <div class="abs brand"><span class="dot"></span>Dorne's Bakery</div>
  <h1 class="abs product-name">Coconut Cream</h1>
  <div class="abs product-type">Bread</div>
  <span class="double-rule left"></span>
  <span class="double-rule right"></span>
  <div class="abs netto">NETTO : 125 gr</div>

  <!-- nutrition facts -->
  <section class="abs nutrition">
    <h2>INFORMASI NILAI GIZI / NUTRITION INFORMATION</h2>
    <div class="gap"></div>
    <div class="nrow"><span class="lbl">Takaran Saji / Service Size</span><span></span><span class="pct">20gr</span></div>
    <div class="nrow"><span class="lbl">Sajian per Kemasan / Serving per Package</span><span></span><span class="pct">4</span></div>
    <div class="bar-thick"></div>
    <div class="nrow head"><span class="lbl">JUMLAH PER SAJIAN / AMOUNT PER SERVING</span><span></span><span></span></div>
    <div class="nrow bold"><span class="lbl">Energi Total / Total Energy</span><span></span><span class="pct">100 kkal/kcal</span></div>
    <div class="nrow sub"><span class="lbl">Energi dari Lemak / Energy from Fat</span><span></span><span class="pct">45 kkal/kcal</span></div>
    <div class="bar-thin"></div>
    <div class="dv-head">%AKG* / %DV*</div>
    <div class="nrow bold"><span class="lbl">Lemak Total / Total Fat</span><span class="amt">5gr</span><span class="pct">8%</span></div>
    <div class="nrow sub"><span class="lbl">Lemak Trans / Trans Fat</span><span class="amt">0gr</span><span class="pct"></span></div>
    <div class="nrow sub"><span class="lbl">Kolesterol / Cholesterol</span><span class="amt">0mg</span><span class="pct"></span></div>
    <div class="nrow bold"><span class="lbl">Lemak Jenuh / Saturated Fat</span><span class="amt">2.5gr</span><span class="pct">0%</span></div>
    <div class="nrow bold"><span class="lbl">Protein / Protein</span><span class="amt">0gr</span><span class="pct">12%</span></div>
    <div class="nrow bold"><span class="lbl">Karbohidrat Total / Total Carbohydrate</span><span class="amt">14gr</span><span class="pct">0%</span></div>
    <div class="nrow sub"><span class="lbl">Serat Pangan / Dietary Fiber</span><span class="amt">2gr</span><span class="pct">4%</span></div>
    <div class="nrow bold"><span class="lbl">Gula / Sugar</span><span class="amt">1gr</span><span class="pct">5%</span></div>
    <div class="nrow bold"><span class="lbl">Natrium / Sodium</span><span class="amt">210 mg</span><span class="pct">14%</span></div>
    <div class="bar-thin"></div>
    <div class="nrow"><span class="lbl">Mineral / Mineral</span><span></span><span></span></div>
    <div class="nrow sub"><span class="lbl">Kalsium / Calcium</span><span></span><span class="pct">6%</span></div>
    <div class="bar-thick"></div>
    <p class="footnote">*&nbsp; Persen AKG berdasarkan kebutuhan energi 2150 kkal. Kebutuhan energi anda mungkin lebih tinggi atau lebih rendah.</p>
    <p class="footnote">*&nbsp; Percent Daily Value is based on 2,150 kcal diet. Your Daily Value may be higher or lower</p>
  </section>

  <!-- ingredients -->
  <h3 class="abs heading ingredients-title">Ingredients <small>:</small></h3>
  <p class="abs ingredients">Aqua, Tea Tree Water, Jeju Cantella Asiatica, Vitamin C, Salicylic Acid, Liquorice Extract, Niacinamide, Polyacrylamide, Dimethicone,Sunflower (Helianthus annuus) seed oil, C13-14 isoparaffin, Laureth-7, Tocopherol, Phenoxyethanol, Ethylparaben, Methylparaben, Butylparaben, Propylparaben.</p>

  <!-- producer & service -->
  <h3 class="abs heading producer-title">Production By :</h3>
  <p class="abs contact producer">Dorne's<br>Bakery &amp; Cake</p>
  <h3 class="abs heading service-title">Consumer Service</h3>
  <p class="abs contact service">0 2468 1357 024<br>Email : care@dornesbakery.com<br>Website : www.dornesbakery.com</p>

  <!-- disposal icons -->
  <div class="abs disposal">
    <svg width="32" height="30" viewBox="0 0 32 30" aria-label="Recyclable">
      <g fill="none" stroke="#000" stroke-width="4" stroke-linejoin="round">
        <polyline points="10,12 16,3 21,11"/>
        <polyline points="24,16 29,26 18,26"/>
        <polyline points="13,26 3,26 8,17"/>
      </g>
    </svg>
    <svg width="28" height="30" viewBox="0 0 28 30" aria-label="Dispose in bin">
      <circle cx="21" cy="3" r="2.6" fill="#000"/>
      <path d="M18 7h6v11h-1.5v11h-1.5v-11h-0.5v11h-1.5v-11h-1z" fill="#000"/>
      <path d="M2 14h11l-1.5 14h-8z" fill="none" stroke="#000" stroke-width="1.6"/>
      <line x1="18" y1="9" x2="11" y2="12" stroke="#000" stroke-width="1.6"/>
    </svg>
  </div>
  <p class="abs dates">Best Before<br>Production Code</p>
</main>
</body>
</html>
```